Lumora Digital - Layout Design

We need a web design for a new company based in Australia, called "Lumora Digital". We develop innovative custom web applications for Out Of Home, and Media companies.
Our initial website is a one page type of site. I've created a simple wireframe to show you what we need: https://sketchplot.example/k3Tq9W
Here is a layout reference: http://folvex.example/
( note - the designs needs to follow our branding guidelines (attached).
The top feature could be just solid color or an abstract subtle pattern or illustration that conveys the specialization of our business in the area of out of home, map, data.
In the attachment you will also find some images added for the work section.
Updates
Target Market(s)
Media and Advertising
Industry/Entity Type
Digital
Number of Pages Required
1 page
Look and feel
Each slider illustrates characteristics of the customer's brand and the style your logo design should communicate.

```html
<!DOCTYPE html>
<html lang="en">
<head>
<meta charset="utf-8">
<title>Lumora Digital</title>
<link href="https://fonts.googleapis.com/css2?family=Open+Sans:wght@400;600;700&display=swap" rel="stylesheet">
<style>
:root{
  --red:#e8412c;
  --ink:#333333;
  --muted:#777777;
  --line:#cfcfcf;
  --paper:#ffffff;
  --grey:#e9e9e9;
  --footer:#2f2f2f;
  --social:#3b82c4;
}
*{box-sizing:border-box;margin:0;padding:0}
html,body{width:1200px;height:3200px;overflow:hidden}
body{font-family:"Open Sans",Arial,sans-serif;color:var(--ink);background:var(--paper);font-size:14px;line-height:1.6}
.site-header{height:64px;border-top:4px solid var(--red);display:flex;align-items:center;justify-content:space-between;padding:0 48px;background:var(--paper)}
.brand{display:flex;align-items:center;gap:8px;font-size:26px;font-weight:600;color:var(--ink);letter-spacing:-.5px}
.brand-dot{width:12px;height:12px;border-radius:50%;background:var(--red)}
.main-nav{display:flex;font-size:12px;font-weight:600;text-transform:uppercase}
.main-nav a{color:var(--ink);text-decoration:none;padding:0 10px;border-left:1px solid var(--line);line-height:12px}
.main-nav a:first-child{border-left:none}
.main-nav a.active{color:var(--red)}

.hero{position:relative;height:456px;overflow:hidden}
.hero-media{position:absolute;inset:0;background:linear-gradient(115deg,#c21d5c 0%,#e44a2a 18%,#f2b81f 34%,#5fbf3a 50%,#1fa3d6 66%,#5b3fb8 82%,#c21d5c 100%)}
.hero-shade{position:absolute;inset:0;background:radial-gradient(ellipse at 50% 40%,rgba(0,0,0,.15),rgba(0,0,0,.45))}
.hero-arrow{position:absolute;top:270px;width:36px;height:36px;border-radius:50%;border:2px solid rgba(255,255,255,.8)}
.hero-arrow.prev{left:70px}
.hero-arrow.next{right:70px}
.hero-caption{position:absolute;left:0;right:0;top:330px;text-align:center;color:#fff}
.hero-caption h1{font-size:26px;font-weight:400;letter-spacing:1px;text-transform:uppercase}
.hero-caption p{font-size:12px;max-width:560px;margin:6px auto 0;opacity:.9}

.section-title{display:flex;align-items:center;justify-content:center;gap:18px;font-size:15px;font-weight:700;letter-spacing:1px;text-transform:uppercase;color:var(--ink)}
.section-title::before,.section-title::after{content:"";width:230px;height:1px;background:var(--line)}

.about{height:200px;padding-top:40px;text-align:center}
.about p{max-width:1000px;margin:16px auto 0;font-size:13px;color:var(--muted)}

.team{height:440px;background:var(--grey);padding-top:36px;text-align:center}
.team-row{display:flex;justify-content:center;align-items:center;gap:26px;margin-top:30px}
.avatar{border-radius:50%;background:linear-gradient(160deg,#b9b3ad,#6f6863)}
.avatar.small{width:70px;height:70px}
.avatar.large{width:112px;height:112px;border:4px solid #fff}
.member-name{margin-top:12px;font-size:13px;font-weight:600}
.dots{display:flex;justify-content:center;gap:8px;margin-top:12px}
.dots span{width:9px;height:9px;border-radius:50%;background:#bdbdbd}
.dots span.on{background:var(--red)}
.quote{max-width:820px;margin:18px auto 0;font-size:13px;font-style:italic;color:var(--muted)}

.board{height:380px;padding-top:36px;text-align:center;position:relative}
.board-row{display:flex;justify-content:center;gap:18px;margin-top:34px}
.advisor{width:84px;height:84px;background:linear-gradient(160deg,#c9c4bf,#7c7570);border:3px solid #fff;box-shadow:0 0 0 1px var(--line)}
.advisor.on{box-shadow:0 0 0 2px var(--red)}
.board-next{position:absolute;right:390px;top:130px;width:26px;height:26px;background:var(--red)}
.advisor-name{margin-top:16px;font-size:12px;font-weight:600;color:var(--red)}
.board .quote{margin-top:10px}

.services{height:220px;background:var(--grey);padding-top:50px;text-align:center}
.services p{max-width:760px;margin:18px auto 0;font-size:13px;color:var(--muted)}

.experience{height:1200px;padding-top:48px}
.project{display:flex;gap:50px;margin:44px 0 0 150px;height:226px}
.project-media{width:300px;height:190px;flex:none}
.project-body{width:500px;padding-top:4px}
.project-body h3{font-size:13px;font-weight:700;text-transform:uppercase;padding-bottom:8px;border-bottom:1px solid var(--line);margin-bottom:10px}
.project-body p{font-size:12.5px;color:var(--muted);margin-bottom:8px}

.contact{height:180px;background:var(--grey);padding-top:20px}
.contact .section-title{font-size:14px}
.contact-grid{display:flex;justify-content:space-between;padding:16px 140px 0 140px}
.contact-brand .brand{font-size:22px}
.socials{display:flex;gap:6px;margin-top:10px}
.socials span{width:20px;height:20px;background:var(--social)}
.newsletter h4{font-size:12px;font-weight:600;color:var(--red);margin-bottom:6px}
.field{width:170px;height:22px;background:#fff;border:1px solid var(--line);margin-bottom:6px}
.submit{display:inline-block;background:var(--red);color:#fff;font-size:10px;font-weight:700;padding:2px 10px}
.details{font-size:12px;color:var(--muted)}
.details li{list-style:none;display:flex;gap:10px;align-items:flex-start;margin-bottom:8px}
.details svg{flex:none;margin-top:2px}

.site-footer{height:60px;background:var(--footer);color:#ddd;font-size:12px;font-weight:600;display:flex;align-items:center;justify-content:center;text-transform:uppercase}
</style>
</head>
<body>
<header class="site-header">
  <div class="brand">Lumora Digital <span class="brand-dot"></span></div>
  <nav class="main-nav">
    <a href="#about">About us</a><a href="#team">Team</a><a href="#services">Services</a><a class="active" href="#experience">Experience</a><a href="#contact">Contact</a>
  </nav>
</header>

<section class="hero">
  <div class="hero-media" role="img" aria-label="Colourful close-up of glittering light with a screen at the centre"></div>
  <div class="hero-shade"></div>
  <span class="hero-arrow prev"></span>
  <span class="hero-arrow next"></span>
  <div class="hero-caption">
    <h1>Lorem ipsum dolor sit amet</h1>
    <p>Custom web applications for out of home and media companies, built around maps, data and the screens people pass every day.</p>
  </div>
</section>

<section class="about" id="about">
  <h2 class="section-title">About us</h2>
  <p>We are Lumora Digital. A team of innovators, thinkers and doers working collaboratively towards our goal. With decades of experience between us from a variety of sources, Lumora Digital is a business focused on helping organisations gain more value from information, through insight and action.</p>
</section>

<section class="team" id="team">
  <h2 class="section-title">Key team</h2>
  <div class="team-row">
    <div class="avatar small" role="img" aria-label="Portrait of a team member"></div>
    <div class="avatar large" role="img" aria-label="Portrait of the CEO"></div>
    <div class="avatar small" role="img" aria-label="Portrait of a team member"></div>
  </div>
  <div class="member-name">Dana Holloway - CEO</div>
  <div class="dots"><span></span><span class="on"></span><span></span></div>
  <p class="quote">"Sed ut perspiciatis unde omnis iste natus error sit voluptatem accusantium doloremque laudantium, totam rem aperiam, eaque ipsa quae ab illo inventore veritatis et quasi architecto beatae vitae dicta sunt explicabo."</p>
</section>

<section class="board">
  <h2 class="section-title">Board of advisors</h2>
  <div class="board-row">
    <div class="advisor" role="img" aria-label="Portrait of an advisor"></div>
    <div class="advisor" role="img" aria-label="Portrait of an advisor"></div>
    <div class="advisor on" role="img" aria-label="Portrait of the selected advisor"></div>
    <div class="advisor" role="img" aria-label="Portrait of an advisor"></div>
  </div>
  <span class="board-next"><svg width="26" height="26" viewBox="0 0 26 26"><path d="M11 8l5 5-5 5" fill="none" stroke="#fff" stroke-width="2"/></svg></span>
  <div class="advisor-name">Jesse Marlow - CTO</div>
  <p class="quote">"Sed ut perspiciatis unde omnis iste natus error sit voluptatem accusantium doloremque laudantium, totam rem aperiam, eaque ipsa quae ab illo inventore veritatis et quasi architecto beatae vitae dicta sunt explicabo."</p>
</section>

<section class="services" id="services">
  <h2 class="section-title">Services</h2>
  <p>Sed ut perspiciatis unde omnis iste natus error sit voluptatem accusantium doloremque laudantium, totam rem aperiam, eaque ipsa quae ab illo inventore veritatis et quasi architecto beatae vitae dicta sunt explicabo.</p>
</section>

<section class="experience" id="experience">
  <h2 class="section-title">Experience</h2>

  <article class="project">
    <div class="project-media" role="img" aria-label="Arvo Outdoor website on a laptop screen" style="background:linear-gradient(135deg,#1b3a6b,#3fa0d8 55%,#e8412c)"></div>
    <div class="project-body">
      <h3>Arvo Outdoor</h3>
      <p>A confident, modern website for an outdoor media network, showing off a fresh visual identity and a full catalogue of sites across the region.</p>
      <p>Hands-on campaign planning tools let buyers map, compare and book locations, making Arvo a clear leader in outdoor media.</p>
    </div>
  </article>

  <article class="project">
    <div class="project-media" role="img" aria-label="Streaks of coloured light for the bidding platform" style="background:linear-gradient(135deg,#0f1a2e,#2fb1e0 45%,#9be23c 70%,#0f1a2e)"></div>
    <div class="project-body">
      <h3>Bidlane - Marketing Bidding Platform</h3>
      <p>Bidlane brings media buyers and suppliers together in one place, with tools for briefs, quotes, approvals, live bidding, supplier profiles and signed agreements.</p>
    </div>
  </article>

  <article class="project">
    <div class="project-media" role="img" aria-label="Digital poster screen in a shopping centre" style="background:linear-gradient(135deg,#0d2233,#2d6f8f 55%,#b9d6e2)"></div>
    <div class="project-body">
      <h3>Iris Media</h3>
      <p>A clean, lively website that leads visitors straight to what Iris offers, backed by guides and case studies that give them good reason to come back.</p>
    </div>
  </article>

  <article class="project">
    <div class="project-media" role="img" aria-label="Taskcloud dashboard on a screen" style="background:linear-gradient(180deg,#f4f4f4,#cfd8d0 60%,#7fa36a)"></div>
    <div class="project-body">
      <h3>Taskcloud</h3>
      <p>Sed ut perspiciatis unde omnis iste natus error sit voluptatem accusantium doloremque laudantium, totam rem aperiam, eaque ipsa quae ab illo inventore veritatis et quasi architecto beatae vitae dicta sunt explicabo.</p>
    </div>
  </article>
</section>

<section class="contact" id="contact">
  <h2 class="section-title">Contact</h2>
  <div class="contact-grid">
    <div class="contact-brand">
      <div class="brand">Lumora Digital <span class="brand-dot"></span></div>
      <div class="socials"><span></span><span></span><span></span><span></span></div>
    </div>
    <div class="newsletter">
      <h4>Newsletter</h4>
      <div class="field"></div>
      <div class="field"></div>
      <span class="submit">SUBMIT</span>
    </div>
    <ul class="details">
      <li><svg width="14" height="12" viewBox="0 0 14 12"><rect x="1" y="1" width="12" height="10" fill="none" stroke="#e8412c" stroke-width="1.5"/><path d="M1 1l6 5 6-5" fill="none" stroke="#e8412c" stroke-width="1.5"/></svg>info@lumoradigital.example</li>
      <li><svg width="14" height="14" viewBox="0 0 14 14"><path d="M3 1l3 3-2 2c1 2 2 3 4 4l2-2 3 3-2 2C6 13 1 8 1 3z" fill="#e8412c"/></svg>02 5550 1234</li>
      <li><svg width="14" height="16" viewBox="0 0 14 16"><path d="M7 1a5 5 0 015 5c0 4-5 9-5 9S2 10 2 6a5 5 0 015-5z" fill="#e8412c"/><circle cx="7" cy="6" r="2" fill="#fff"/></svg>Level 9, 42 Harbour Lane,<br>Sydney NSW 2000 Australia</li>
    </ul>
  </div>
</section>

<footer class="site-footer">© Copyright by 2015 and all right reserved by company</footer>
</body>
</html>
```